Business Card Design

I'm a Naturopathic Physician specializing in the treatment of autoimmune disorders, supportive cancer care and stress, anxiety and depressive disorders.

I practice out of 3 clinic locations and I want a business card design which can be easily changed to include 3 clinic locations, addresses, and contact info.

My website is VeltarisHealth.com and this will promote me personally as a specialist in these treatment areas. I would like one side of the business card to promote this site with the tag line "Specializing in Immune and Related Disorders"

REVIEW THE DESCRIPTION AND UPLOADS FOR MY DESIGN STYLE PREFERENCES.

Industry/Entity Type

Clinic

Colors
9bcb3c
fbed22
0455a3

Requirements
Must have
• Would prefer a vertical design.
Would like bold, simple colors and contrasts

Please visit http://plovexa.com/veltarishealth/ for some color and design "feel"

Do not feel the Designs HAVE to have the logo in it... I want SIMPLE, CLEAN and BOLD design so if the Logo makes the designs too busy, please omit

Dr. Marcus Fenholt BSc ND
Naturopathic Physician

"Clinic Name"
"Clinic Address"
"Clinic Tel"
"Clinic E-Mail"
"Clinic Website"

Please review the PDF for design styles I prefer.

Please Note: Once I determine if there are design concepts worthy of going forward with, I will forward specific contact and clinic information at that time for final design

```html
<!DOCTYPE html>
<html lang="en">
<head>
<meta charset="utf-8">
<title>VeltarisHealth.com – Business Card</title>
<link rel="stylesheet" href="https://fonts.googleapis.com/css2?family=Arimo:ital,wght@0,400;0,700;1,700&display=swap">
<style>
  :root {
    --brand-blue: #0149a0;
    --brand-green: #9fc41a;
    --circle-green: #8db52a;
    --paper: #ffffff;
    --stage: #ffffff;
    --ink-white: #ffffff;
  }
  html, body {
    margin: 0;
    width: 1200px;
    height: 899px;
    overflow: hidden;
    background: var(--stage);
    font-family: "Arimo", Arial, Helvetica, sans-serif;
  }
  .stage {
    position: relative;
    width: 1160px;
    height: 869px;
    transform: scale(1.0345);
    transform-origin: 0 0;
  }
  .card {
    position: absolute;
    left: 320px;
    width: 532px;
    height: 325px;
    box-shadow: 0 6px 22px rgba(0,0,0,0.22);
    overflow: hidden;
  }
  .card--front { top: 81px; background: var(--brand-blue); }
  .card--back  { top: 471px; background: var(--paper); }

  .band {
    position: absolute;
    left: 0;
    width: 502px;
    background: var(--brand-green);
    border-radius: 0 10px 10px 0;
  }
  .card--front .band { top: 174px; height: 30px; }
  .card--back .band  { top: 70px; height: 47px; border-radius: 0 14px 14px 0; }

  .mark-circle {
    position: absolute;
    left: 29px;
    width: 94px;
    height: 94px;
    border-radius: 50%;
    background: var(--circle-green);
  }
  .card--front .mark-circle { top: 115px; }
  .card--back .mark-circle  { top: 47px; }

  .site-name {
    position: absolute;
    left: 137px;
    top: 126px;
    margin: 0;
    font-size: 39px;
    font-weight: 700;
    line-height: 1;
    letter-spacing: -0.5px;
    color: var(--ink-white);
    white-space: nowrap;
  }
  .tagline {
    position: absolute;
    left: 137px;
    top: 182px;
    margin: 0;
    font-size: 15.5px;
    font-weight: 700;
    font-style: italic;
    line-height: 1;
    color: var(--ink-white);
    white-space: nowrap;
  }

  .person {
    position: absolute;
    left: 158px;
    top: 76px;
    color: var(--ink-white);
  }
  .person__name {
    margin: 0;
    font-size: 20px;
    font-weight: 700;
    line-height: 1;
  }
  .person__creds {
    font-size: 14px;
    font-weight: 400;
  }
  .person__title {
    margin: 4px 0 0;
    font-size: 14.5px;
    line-height: 1;
  }

  .clinic {
    position: absolute;
    left: 159px;
    top: 147px;
    height: 148px;
    padding-left: 29px;
    border-left: 2px solid var(--brand-blue);
    color: var(--brand-blue);
  }
  .clinic__name {
    margin: 0;
    font-size: 19px;
    font-weight: 700;
    line-height: 1;
  }
  .clinic__address {
    margin: 9px 0 0;
    font-style: normal;
    font-size: 15px;
    line-height: 19px;
  }
  .clinic__contacts {
    margin: 7px 0 0;
    padding: 0;
    list-style: none;
    font-size: 15px;
    line-height: 18.5px;
  }
  .clinic__label {
    display: inline-block;
    width: 27px;
    font-weight: 700;
  }
</style>
</head>
<body>
<div class="stage">

  <section class="card card--front" aria-label="Business card front">
    <div class="band"></div>
    <div class="mark-circle"></div>
    <h1 class="site-name">VeltarisHealth.com</h1>
    <p class="tagline">Specializing in Immune and Related Disorders</p>
  </section>

  <section class="card card--back" aria-label="Business card back">
    <div class="band"></div>
    <div class="mark-circle"></div>
    <div class="person">
      <h2 class="person__name">Dr. Marcus Fenholt <span class="person__creds">BSc ND</span></h2>
      <p class="person__title">Naturopathic Physician</p>
    </div>
    <div class="clinic">
      <h3 class="clinic__name">Harborview Osteopathic Clinic</h3>
      <address class="clinic__address">42 Mill Lane,<br>Harborview, N.S.<br>B0R 2K4</address>
      <ul class="clinic__contacts">
        <li><span class="clinic__label">T:</span>902.555.0148</li>
        <li><span class="clinic__label">E:</span>info@harborviewclinic.com</li>
        <li><span class="clinic__label">W:</span>www.HarborviewClinic.com</li>
      </ul>
    </div>
  </section>

</div>
</body>
</html>
```